New Website for Asia Travel Agency

Lanternpath Journeys Website

We want a redesign for our current website, www.lanternpathjourneys.example. We want you to get creative with our brand and present our company in a unique, creative and compelling way, that communicates our exotic destinations and tours, the local and authentic character of our travel consultants and the trustworthy and professional nature of our company.

Who is this company?

Lanternpath Journeys is an online tour operator specializing in providing tailor-made tours to eight destinations in Asia; Vietnam, Thailand, Laos, Cambodia, Indonesia, Myanmar, Japan and China. They were launched in mid February 2012 with headquarters in Bangkok, Thailand, and staffed by locals and expats with many years of experience in the travel industry, and who are committed to sharing their deep knowledge of, and passion for the region.

Local knowledge

Our consultants at Lanternpath Journeys are all locals – they know their destinations inside-out and draw upon invaluable first-hand experience and information when planning your tour. They have insights into local culture and tradition, they know the best places to visit, the most worthwhile experiences to have and, most importantly, they have the knowledge to create exactly the holiday you desire.

All hotels and activities featured in a Lanternpath Journeys tour are regularly inspected by our consultants to ensure the highest quality standards are met and that all information is correct and up to date.

Unforgettable Travel Experiences

Whether it's a cultural exploration or a beach holiday you're after – or a mix of both – Lanternpath Journeys has an itinerary for you – and if we don't have one, we'll tailor-make one! From the main sights to remote villages, our locally based Travel Specialists will give you unique insights into every place you visit and let you delve into known destinations from new perspectives.

Our tours offer a variety of hotel and resort options, premium stays in deluxe accommodation, heritage hotels, a five-star boutique or on the water in a junk. Tap into our experience let us create an experience unique to you – and one you will never forget.

What type of Holiday to Asia?

Our itineraries at Lanternpath Journeys are created according to different inspirations. Some travelers are interested in the History & Culture of a destination, while some like to stay active with Adventure tours. A Cross Border trip explores different countries in a single tour, while Velvet Summit tours offer the highest level of exclusivity across our destinations. There are 14 different Holiday Types to choose from, or you can mix and match ideas to create your dream vacation.

Target Market(s)

Slightly more female, aged 30-65, are creative, professional and looking for something different, something a bit unusual.

Industry/Entity Type

Boutique

Requirements
Must have
• 5 page designs:

1. Homepage
2. Tours list page for a country
3. Tour page
4. 'Be Inspired' page
5. Country page
6. Enquiry page

Our inspirations.

The following list shows websites we love and which inspire us... to give you some indication of our preferred styles, functions and layouts:

http://www.frostmeridian.example/en/ (we really like this, great personality, like the use of icons for tour types)
http://www.pebblewalks.example.uk/ (very simple design elements and layout)
http://www.sunvalecoast.example/ (great use of background image, nice simple nav bar)
http://www.roamcedarfall.example/ (we like because it has distinct personality and is well suited to the destination)
http://www.seemarlowton.example/ (clear personality through font use)
http://www.vastroving.example/ (original, unique)
http://www.wanderquill.example/long-loop-of-asia (like the map style)

Key design points:

1. You must use our existing logo (attached), but you can change the color scheme of the logo to accord with the whichever color scheme you choose for the main designs.
2. Our logo strapline is "Asia is our Lanternpath" and should be used prominently on the page to reinforce the meaning of our company name.
3. Home page and tours list pages should allow the user to see the choice of tours immediately without scrolling & Introduction copy should be minimal.
4. We and our site visitors are inspired and excited by our photography, this is an element of the site which we would like to maintain and build on, though the section page header sliders are currently too big and do not allow quick access to the section content. This is a design problem which needs a solution. Full page photographic backgrounds may be an answer?
5. Tour page should display other contextual tours, from the same country or style/type
6. We should promote press coverage in various places
7. We should display consultant profiles in various places
8. Map designs for tour page and country page, plus a modal pop out for the home page. These are complex and may have a few small photos and short descriptive text only, though this is limited by your own creativity. We will use graphics and html5/css3 so there are no creative limitations.
9. The 'Inspirations' / 'Be Inspired' page is for people who want travel and holiday ideas, who are looking for inspiration on where to go and what to do. This section needs to reflect the exotic, the unusual, the extraordinary in our destinations and tours, and we leave this to your creative genius to develop. We are also interested in how this inspirations page is related to the blog and social media content we produce daily, is there an integration here? Can we present YouTube videos, our blog posts, Facebook posts etc, on this page? This is another design challenge.
10. We would like to see designs for the tours list page which feature AJAX content filtering (for instance: http://demo.layoutbrisk.example/?acn), we would like to see how to include this type of content filtering on homepage and destination page also.
11. The 'Enquiry' call to action should be on all pages and prominent.
12. The enquiry page can reflect the same fields as the existing website enquiry page

Values to be communicated:

- Exotic: Asia is exotic, and our tours will expose clients to extraordinary sights and unusual cultural encounters.
- Authentic: Our travel consultants all live in the destinations themselves, they are local nationals and have all the insider knowledge to give clients a truly authentic experience of our destinations
- Unique: All of our tours are tailor made, there are no fixed departure dates or join-in groups. All tour itineraries can be uniquely designed for our clients, from departure dates to destinations.
- Trust: Some travelers prefer to book their holidays with local agencies they can meet in person, rather than with online companies like us who live in the destinations and who they only get to meet on Skype video or phone. We want to convey that we are trustworthy. We have attempted this through presenting a 'meet the team' page and a 'press' page and advert, as well as offering a prominent international phone number. How we you build on this and further convey this value?

```html
<!DOCTYPE html>
<html lang="en">
<head>
<meta charset="utf-8">
<title>Lanternpath Journeys – Asia is our Lanternpath</title>
<link rel="stylesheet" href="https://fonts.googleapis.com/css2?family=Source+Sans+3:wght@400;600;700&display=swap">
<style>
:root{
  --red:#e2261e;
  --red-dark:#c41c15;
  --ink:#222;
  --text:#555;
  --muted:#777;
  --bar:#111;
  --footer:#1f242b;
  --footer-text:#c9ccd1;
  --panel:#eeeeee;
  --line:#d5d5d5;
  --white:#fff;
  --teal:#8fc3c4;
  --link:#2a5aa5;
  --orange:#e08a12;
}
*{box-sizing:border-box;margin:0;padding:0}
h1,h2,h3,h4,h5{font-weight:400}
html,body{width:1200px;height:2222px;overflow:hidden}
body{position:relative;font-family:"Source Sans 3",Arial,sans-serif;color:var(--text);background:var(--teal)}
a{color:inherit;text-decoration:none}

/* top bar */
.topbar{position:absolute;left:0;top:0;width:1200px;height:33px;background:var(--bar)}
.topbar__links{position:absolute;left:111px;top:10px;font-size:10px;font-weight:700;color:#fff;letter-spacing:.2px;text-transform:uppercase}
.topbar__links span{padding:0 6px;border-left:1px solid #fff}
.topbar__links span:first-child{padding-left:0;border-left:0}
.topbar__social{position:absolute;left:659px;top:9px;display:flex;gap:11px}
.topbar__social i{display:block;width:15px;height:15px;border-radius:50%;background:#fff}
.search{position:absolute;left:870px;top:4px;width:176px;height:27px;background:#fff;font-size:14px;color:#333;padding:4px 7px}
.search__go{position:absolute;left:1046px;top:4px;width:40px;height:27px;background:var(--red);color:#fff;font-size:13px;font-weight:600;text-align:center;line-height:27px}

/* header */
.header{position:absolute;left:0;top:33px;width:1200px;height:74px;background:rgba(255,255,255,.94)}
.logo{position:absolute;left:108px;top:5px;width:231px;height:69px;background:var(--red);color:#fff;display:flex;align-items:center;gap:10px;padding-left:14px}
.logo__mark{width:20px;height:20px;border-radius:50%;background:#fff;flex:none}
.logo__name{font-size:17px;font-weight:700;line-height:1.05;white-space:nowrap}
.logo__name small{display:block;font-size:11px;font-weight:700;margin-top:3px;text-align:right}
.nav{position:absolute;left:395px;top:31px;display:flex;font-size:16px;color:#222;text-transform:uppercase}
.nav a{margin-right:27px}
.nav a.is-active{font-weight:600}
.nav a:last-child{margin-right:0}

/* hero / page photo */
.page-photo{position:absolute;left:0;top:107px;width:1200px;height:1837px;
  background:
    radial-gradient(ellipse 70px 130px at 760px 220px,rgba(120,55,25,.75),rgba(120,55,25,0) 100%),
    radial-gradient(ellipse 230px 70px at 660px 200px,rgba(40,85,40,.95),rgba(40,85,40,0) 100%),
    radial-gradient(ellipse 180px 60px at 1080px 240px,rgba(230,120,50,.35),rgba(230,120,50,0) 100%),
    radial-gradient(ellipse 500px 160px at 150px 520px,rgba(235,232,222,.75),rgba(235,232,222,0) 100%),
    linear-gradient(180deg,#4e86cf 0%,#86b2e2 5%,#d6e6f3 11%,#3aa7bb 13%,#58bcc4 18%,#a7dbd6 24%,#d7ece6 30%,#bcdcd8 38%,#9ccbca 55%,#8fc3c4 75%,#8cbfc1 100%)}
.hero-caption{position:absolute;left:110px;top:285px;width:453px}
.hero-caption__title{height:56px;background:rgba(255,255,255,.82);color:var(--red);font-size:32px;font-weight:700;padding:5px 0 0 12px}
.hero-caption__text{height:96px;background:rgba(35,35,35,.8);color:#fff;font-size:16.5px;line-height:24px;padding:8px 12px}
.hero-caption__text b{color:var(--red)}
.slider-dots{position:absolute;left:1013px;top:609px;display:flex;gap:3px}
.slider-dots i{width:9px;height:9px;background:#fff;display:block}
.slider-dots i.is-on{background:var(--red)}

/* content sheet */
.sheet{position:absolute;left:95px;top:630px;width:1019px;height:1314px;background:#fff}

.welcome__title{position:absolute;left:116px;top:664px;font-size:28px;color:var(--ink)}
.welcome__rule{position:absolute;left:116px;top:701px;width:460px;height:1px;background:#bbb}
.welcome__body{position:absolute;left:118px;top:722px;width:470px;font-size:15.5px;line-height:22px;color:#444}
.welcome__body p{margin-bottom:19px}
.welcome__more{color:var(--red);font-size:13px;display:block;margin-top:-19px}

/* booking widget */
.booking{position:absolute;left:630px;top:671px;width:469px;height:277px;background:#fff;border:1px solid #ddd;box-shadow:0 10px 12px -8px rgba(0,0,0,.3)}
.booking__title{position:absolute;left:10px;top:10px;font-size:16px;color:var(--red);font-weight:600}
.booking__title small{font-size:8px;color:#888;font-weight:400}
.booking__tabs{position:absolute;left:15px;top:42px;width:225px;height:30px;background:var(--red);display:flex}
.booking__tabs span{flex:1;border-right:1px solid #fff;display:flex;align-items:center;justify-content:center}
.booking__tabs span:first-child{background:#d21d15}
.booking__tab-label{position:absolute;left:15px;top:72px;width:225px;height:15px;background:var(--red);color:#fff;font-size:11px;font-weight:700;padding-left:6px;line-height:15px}
.field-label{position:absolute;font-size:11px;color:#555;line-height:13px}
.field{position:absolute;height:19px;border:1px solid #bbb;font-size:10.5px;color:#777;padding:2px 5px;background:#fff;line-height:13px}
.cal{position:absolute;width:17px;height:19px;background:var(--red);color:#fff;font-size:9px;font-weight:700;text-align:center;line-height:19px}
.field-note{position:absolute;font-size:9px;color:#888}
.check{position:absolute;font-size:11px;color:#555;padding-left:17px}
.check::before{content:"";position:absolute;left:0;top:2px;width:11px;height:11px;border:1px solid #aaa;background:#f3f3f3}
.booking__callout{position:absolute;left:265px;top:41px;width:195px;height:96px;background:#fff;border:1px solid #ddd;box-shadow:2px 3px 4px rgba(0,0,0,.15);padding:7px 10px}
.booking__callout::before{content:"";position:absolute;left:-9px;top:10px;border:8px solid transparent;border-right-color:#ddd;border-left:0}
.booking__callout h4{font-size:13.5px;color:var(--red);font-weight:600;border-bottom:1px solid #ccc;padding-bottom:3px;margin-bottom:4px}
.booking__callout p{font-size:10.5px;line-height:12.5px;color:#666}
.booking__links{position:absolute;left:261px;top:186px;font-size:10.5px;color:var(--link);line-height:18.5px}
.booking__links div{padding-left:17px;position:relative}
.booking__links div::before{content:"";position:absolute;left:0;top:4px;width:10px;height:10px;border:1px solid #aaa;background:#eee}
.booking__divider{position:absolute;left:264px;top:178px;width:196px;height:1px;background:#ddd}

/* promotions */
.promos{position:absolute;left:108px;top:993px;width:993px;height:303px;background:var(--panel);box-shadow:0 2px 4px rgba(0,0,0,.15)}
.promos__title{position:absolute;left:36px;top:19px;font-size:20px;color:var(--ink)}
.promos__tabs{position:absolute;left:290px;top:21px;display:flex;align-items:center;font-size:12.5px;color:#555;text-transform:uppercase}
.promos__tabs span{margin-right:18px}
.promos__tabs .is-on{background:var(--red);color:#fff;border-radius:13px;padding:3px 11px;text-transform:none;font-size:13.5px}
.promo-card{position:absolute;top:68px;width:219px}
.promo-card__img{height:127px;box-shadow:0 2px 3px rgba(0,0,0,.2)}
.promo-card__title{font-size:16.5px;color:var(--red);margin-top:14px}
.promo-card__text{width:205px;font-size:12.5px;line-height:15.5px;color:#666;margin-top:9px}
.promo-card__text b{color:var(--red)}
.arrow-btn{position:absolute;width:28px;height:30px;background:var(--red);display:flex;align-items:center;justify-content:center}

/* tours */
.section-title{position:absolute;font-size:20px;color:var(--red)}
.tours__rule{position:absolute;left:345px;top:1369px;width:391px;height:1px;background:#ccc}
.tour__img{position:absolute;left:116px;width:213px;height:119px}
.tour__dots{position:absolute;display:flex;gap:4px}
.tour__dots i{width:5px;height:5px;background:#fff;display:block}
.tour__span{position:absolute;left:329px;width:53px;height:94px;background:#eee;font-size:12.5px;color:#333;text-align:center;padding-top:6px;line-height:15.5px}
.tour__span b{font-weight:400;display:block;margin-bottom:10px}
.tour__info{position:absolute;left:413px;width:325px;font-size:14px;color:#555;line-height:16.5px}
.tour__info .lbl{color:var(--red)}
.tour__info small{display:block;font-size:8.5px;color:#888;line-height:11px;margin-bottom:16px}
.tour__info p{margin-bottom:14px}
.tour__badge{position:absolute;left:634px;width:62px;height:62px;border-radius:50%;border:3px solid var(--red);background:rgba(226,38,30,.08);box-shadow:inset 0 0 0 5px #fff,inset 0 0 0 7px var(--red);opacity:.85;transform:rotate(-14deg)}
.tour__title{position:absolute;left:117px;font-size:14px;font-weight:700;color:#444;text-transform:uppercase}
.tour__desc{position:absolute;left:117px;width:620px;font-size:12px;line-height:19px;color:#555}
.tour__desc b{color:var(--orange);font-weight:400;margin-left:6px}
.tour__divider{position:absolute;left:117px;top:1625px;width:619px;height:1px;background:#ddd}

/* side */
.side-title{position:absolute;left:794px;top:1329px;font-size:21px;color:var(--ink)}
.map{position:absolute;left:793px;top:1364px;width:300px;height:160px;border:1px solid #cfd8de;
  background:
    radial-gradient(ellipse 60px 140px at 280px 120px,rgba(180,214,232,.95),rgba(180,214,232,0) 100%),
    radial-gradient(ellipse 90px 40px at 80px 150px,rgba(190,218,232,.9),rgba(190,218,232,0) 100%),
    radial-gradient(ellipse 140px 90px at 130px 60px,#f3eedc,rgba(243,238,220,0) 100%),
    linear-gradient(135deg,#f2ecd8 0%,#efe8d2 50%,#d6e6ec 78%,#bcd7e4 100%)}
.map-btn{position:absolute;left:957px;top:1535px;width:136px;height:19px;background:var(--red);color:#fff;font-size:11.5px;line-height:19px;padding-left:22px}
.map-btn::before{content:"";position:absolute;left:8px;top:5px;width:9px;height:9px;border-radius:50%;background:#fff}
.press{position:absolute;left:790px;top:1585px;width:302px;height:329px;background:#fff;border:1px solid #e2e2e2;box-shadow:0 1px 3px rgba(0,0,0,.08)}
.press__head{height:45px;background:linear-gradient(#fff,#f0f0f0);border-bottom:1px solid #e2e2e2;font-size:17px;color:var(--ink);padding:12px 0 0 12px}
.press__cover{position:absolute;width:84px;height:109px;box-shadow:0 1px 3px rgba(0,0,0,.3)}

/* footer */
.footer{position:absolute;left:0;top:1944px;width:1200px;height:278px;background:var(--footer);color:var(--footer-text)}
.footer__col{position:absolute;top:37px}
.footer__col h5{font-size:13.5px;color:#fff;text-transform:uppercase;margin-bottom:17px}
.footer__col li{list-style:none;font-size:12px;line-height:20px}
.footer__col p{font-size:12.5px;line-height:19px;font-style:italic;color:#b8bcc3;width:290px}
.newsletter{position:relative;margin-top:10px;width:298px;height:26px;border-bottom:1px solid #4a5058;font-size:11.5px;font-style:italic;color:#9ba0a8;padding:4px 12px}
.newsletter b{position:absolute;right:12px;top:4px;color:#fff;font-style:normal;font-weight:600}
.footer__social{position:absolute;left:901px;top:209px;display:flex;gap:8px}
.footer__social i{display:block;width:15px;height:15px;border-radius:50%;background:#fff}
.footer__rule{position:absolute;left:107px;top:218px;width:784px;height:1px;background:#4a5058}
.footer__rule--end{left:1032px;width:57px}
.footer__copy{position:absolute;left:107px;top:232px;font-size:11.5px;color:#9ba0a8}
</style>
</head>
<body>

<header class="topbar">
  <nav class="topbar__links"><span>Meeting Planners</span><span>Tour &amp; Travel</span><span>Members</span><span>Media</span></nav>
  <div class="topbar__social" aria-label="Social links"><i></i><i></i><i></i><i></i><i></i><i></i><i></i></div>
  <div class="search">Search</div>
  <div class="search__go">GO</div>
</header>

<div class="page-photo" role="img" aria-label="Long-tail boat moored in turquoise shallows below a green limestone island, swimmers in the sea, white sand in front"></div>

<div class="header">
  <a class="logo" href="#"><span class="logo__mark"></span><span class="logo__name">Lanternpath Journeys<small>Asia is our lanternpath.</small></span></a>
  <nav class="nav">
    <a class="is-active" href="#">Home</a><a href="#">Tours for a country</a><a href="#">Tour</a><a href="#">Be Inspired</a><a href="#">Country</a><a href="#">Enquiry</a><a href="#">Blog</a>
  </nav>
</div>

<section class="hero-caption">
  <h1 class="hero-caption__title">Asia is our Lanternpath</h1>
  <p class="hero-caption__text">No one knows a destination better than someone who lives, works and plays there. That's the foundation of Lanternpath Journeys. <b>»</b></p>
</section>
<div class="slider-dots"><i class="is-on"></i><i></i><i></i><i></i><i></i><i></i></div>

<main class="sheet"></main>

<h2 class="welcome__title">Welcome To Our Website</h2>
<div class="welcome__rule"></div>
<div class="welcome__body">
  <p>No one knows a destination better than someone who lives, works and plays there. That's the foundation of Lanternpath Journeys.</p>
  <p>The result is a travel company tailor-made for the person with a taste for veering off the well-trodden path, for the adventurer who wants access to Asia's most spectacular sights, but hidden charms as well, on the road less traveled.</p>
  <p>Want to explore this Asia? Step into our Lanternpath.</p>
  <a class="welcome__more" href="#">Read More</a>
</div>

<section class="booking">
  <h3 class="booking__title">Search &amp; Book <small>by Lanternpath Journeys</small></h3>
  <div class="booking__tabs">
    <span><svg width="20" height="14" viewBox="0 0 20 14"><rect x="1" y="2" width="3" height="11" fill="#fff"/><rect x="1" y="8" width="18" height="3" fill="#fff"/><rect x="6" y="4" width="12" height="4" fill="#fff"/></svg></span>
    <span><svg width="18" height="16" viewBox="0 0 18 16"><path d="M9 1v14M2 9l7-3 7 3M6 15h6" stroke="#fff" stroke-width="2" fill="none"/></svg></span>
    <span><svg width="18" height="14" viewBox="0 0 18 14"><rect x="2" y="5" width="14" height="6" rx="1" fill="#fff"/><rect x="4" y="1" width="10" height="5" fill="#fff"/><circle cx="5" cy="12" r="2" fill="#fff"/><circle cx="13" cy="12" r="2" fill="#fff"/></svg></span>
    <span><svg width="20" height="14" viewBox="0 0 20 14"><path d="M1 9h18l-3 4H4z" fill="#fff"/><rect x="6" y="3" width="8" height="5" fill="#fff"/></svg></span>
    <span><svg width="20" height="14" viewBox="0 0 20 14"><path d="M2 11h16M4 8h12l2-4H6z" stroke="#fff" stroke-width="2" fill="none"/></svg></span>
  </div>
  <div class="booking__tab-label">Accommodation</div>
  <div class="field-label" style="left:15px;top:92px">Search area, landmark or hotel name:</div>
  <div class="field" style="left:15px;top:108px;width:225px">Area, landmark or property</div>
  <div class="field-label" style="left:15px;top:137px">Type of accommodation:</div>
  <div class="field" style="left:15px;top:152px;width:225px">Hotels
    <svg style="position:absolute;right:2px;top:2px" width="13" height="13" viewBox="0 0 13 13"><rect width="13" height="13" fill="#eee" stroke="#999"/><path d="M3 5h7l-3.5 4z" fill="#333"/></svg>
  </div>
  <div class="field-label" style="left:15px;top:186px">Check in:</div>
  <div class="field" style="left:15px;top:203px;width:84px">01/08/2013</div>
  <div class="cal" style="left:103px;top:203px">31</div>
  <div class="field-note" style="left:15px;top:225px">Thursday</div>
  <div class="field-label" style="left:132px;top:186px">Check out:</div>
  <div class="field" style="left:132px;top:203px;width:84px">02/08/2013</div>
  <div class="cal" style="left:222px;top:203px">31</div>
  <div class="field-note" style="left:132px;top:225px">Friday (1 Night)</div>
  <div class="check" style="left:15px;top:244px">I have no specific dates</div>
  <div class="booking__callout">
    <h4>Book your trip here</h4>
    <p>Wide selection of hotels, cottages, flights, ferry, cruise and rental cars for your trip to and within Lanternpath Journeys</p>
  </div>
  <div class="booking__divider"></div>
  <div class="booking__links"><div>Change my booking</div><div>Help with my booking</div><div>Best price guaranteed</div></div>
</section>

<section class="promos">
  <h2 class="promos__title">Our Featured Promotions</h2>
  <div class="promos__tabs"><span class="is-on">Hot Destinations</span><span>New Creations</span><span>Last Viewed</span></div>

  <article class="promo-card" style="left:27px">
    <div class="promo-card__img" role="img" aria-label="Carved golden temple statue detail from Bali" style="background:radial-gradient(ellipse 120px 40px at 110px 60px,#b99a68,rgba(185,154,104,0)),linear-gradient(135deg,#4a3826,#8f7550 50%,#3e2f22)"></div>
    <h3 class="promo-card__title">Bali Honey Moon</h3>
    <p class="promo-card__text">Enjoy a romantic journey and discover the cultural delights of Bali. Indulge your lover with romantic <b>»</b></p>
  </article>
  <article class="promo-card" style="left:265px">
    <div class="promo-card__img" role="img" aria-label="Aerial view of a green bay with boats in China" style="background:radial-gradient(ellipse 90px 40px at 120px 85px,#2f6f78,rgba(47,111,120,0)),linear-gradient(160deg,#a3b8a8,#3f6c56 45%,#5e8e80)"></div>
    <h3 class="promo-card__title">Epic China</h3>
    <p class="promo-card__text">It's easy to immediately think of the Forbidden City, the Great Wall and the Terracotta <b>»</b></p>
  </article>
  <article class="promo-card" style="left:502px">
    <div class="promo-card__img" role="img" aria-label="Cyclist riding along a railing under a blue sky in Vietnam" style="background:linear-gradient(180deg,#3f6fbf,#9ebde2 45%,#dfe8f0 65%,#c8b48e 100%)"></div>
    <h3 class="promo-card__title">Bike &amp; Paddle Vietnam</h3>
    <p class="promo-card__text">Cycle in the beautiful, quiet Vietnam-ese countryside, through lush fields, down <b>»</b></p>
  </article>
  <article class="promo-card" style="left:741px">
    <div class="promo-card__img" role="img" aria-label="Red lanterns hanging over traditional round Hakka earth houses" style="background:radial-gradient(circle at 40px 50px,#c0281c,rgba(192,40,28,0) 45px),linear-gradient(160deg,#b9cadb,#7d8f66 35%,#6b5a4e 70%,#4a3f38)"></div>
    <h3 class="promo-card__title">Fortresses, Modern History</h3>
    <p class="promo-card__text">This concise and educational 'For-tresses, Modern History &amp; The Hakka' tour takes you to <b>»</b></p>
  </article>
</section>
<a class="arrow-btn" href="#" style="left:89px;top:1114px" aria-label="Previous"><svg width="10" height="12" viewBox="0 0 10 12"><path d="M8 1L2 6l6 5z" fill="#fff"/></svg></a>
<a class="arrow-btn" href="#" style="left:1092px;top:1114px" aria-label="Next"><svg width="10" height="12" viewBox="0 0 10 12"><path d="M2 1l6 5-6 5z" fill="#fff"/></svg></a>

<h2 class="section-title" style="left:117px;top:1341px">Organise your trip to Asia</h2>
<div class="tours__rule"></div>

<article>
  <div class="tour__img" role="img" aria-label="Dim golden temple interior in Myanmar" style="top:1393px;background:radial-gradient(ellipse 60px 50px at 70px 45px,#9a6a35,rgba(154,106,53,0)),linear-gradient(135deg,#3a2412,#7a4e26 50%,#2c1a0d)"></div>
  <div class="tour__dots" style="left:196px;top:1493px"><i></i><i></i><i></i><i></i><i></i><i></i></div>
  <div class="tour__span" style="top:1399px"><b>Weeks<br>08</b>Days<br>13</div>
  <div class="tour__info" style="top:1393px">
    <span class="lbl">Promotion: Price</span> $624 (10% Off)<small>(Price Per Person)</small>
    <p><span class="lbl">Duration:</span> 4 Days / 3 Nights</p>
    <p><span class="lbl">Fast Facts:</span> Romantic in name &amp; alluring in nature, experience 2 of Myanmar's finest; Mandalay &amp; Bagan.</p>
  </div>
  <div class="tour__badge" style="top:1393px"></div>
  <h3 class="tour__title" style="top:1538px">A Tale of Two Cities: Mandalay to Bagan</h3>
  <p class="tour__desc" style="top:1561px">See Mandalay and Bagan and learn about the craftsmanship for which they are famed. Visit villages, monaster-ies and cave temples; meeting locals and trying delicacies along the way. <b>View Tour</b></p>
</article>
<div class="tour__divider"></div>

<article>
  <div class="tour__img" role="img" aria-label="Elephant crossing road sign framed by dark trees in Cambodia" style="top:1656px;background:radial-gradient(ellipse 50px 45px at 140px 55px,#b8a58a,rgba(184,165,138,0)),linear-gradient(160deg,#c8c9c4,#3c3a30 55%,#1e1c16)"></div>
  <div class="tour__span" style="top:1678px"><b>Weeks<br>08</b>Days<br>13</div>
  <div class="tour__info" style="top:1658px">
    <span class="lbl">Promotion: Price</span> $424 (10% Off)<small>(Price Per Person)</small>
    <p><span class="lbl">Duration:</span> 4 Days / 3 Nights</p>
    <p><span class="lbl">Fast Facts:</span> Romantic in name &amp; alluring in nature, experience 2 of Myanmar's finest; Mandalay &amp; Bagan.</p>
  </div>
  <div class="tour__badge" style="top:1659px"></div>
  <h3 class="tour__title" style="top:1802px">Angro Wat Family Adventure</h3>
  <p class="tour__desc" style="top:1826px">See Mandalay and Bagan and learn about the craftsmanship for which they are famed. Visit villages, monaster-ies and cave temples; meeting locals and trying delicacies along the way. <b>View Tour</b></p>
</article>

<h2 class="side-title">Lay of the Land</h2>
<div class="map" role="img" aria-label="Route map through Thailand, Laos, Cambodia and Vietnam from Bangkok via Angkor Wat to Hue and Hoi An"></div>
<a class="map-btn" href="#">Go to detailed map</a>

<aside class="press">
  <h3 class="press__head">Read Our Latest Press Coverage</h3>
  <div class="press__cover" role="img" aria-label="Travel magazine cover with a beach scene" style="left:10px;top:62px;background:linear-gradient(#e8e8e8 0 18%,#3f86b8 18%,#7fb3cf 55%,#c9a87c)"></div>
  <div class="press__cover" role="img" aria-label="Adventure magazine cover in red tones" style="left:108px;top:62px;background:linear-gradient(#c0281c 0 25%,#8c3a2a 25%,#b57a52 60%,#d9b08a)"></div>
  <div class="press__cover" role="img" aria-label="Guide magazine cover with a portrait" style="left:206px;top:62px;background:linear-gradient(#eee8dc 0 22%,#b9a98f 22%,#8b7d6c)"></div>
  <div class="press__cover" role="img" aria-label="Traveller magazine cover in black and white" style="left:10px;top:202px;background:linear-gradient(#d8d8d8 0 20%,#f2f2f2 20%,#9a9a9a 60%,#3c3c3c)"></div>
  <div class="press__cover" role="img" aria-label="In-flight magazine cover in yellow with a temple statue" style="left:108px;top:202px;background:radial-gradient(ellipse 22px 34px at 50px 80px,#9a6a1a,rgba(154,106,26,0)),linear-gradient(#f4c93a,#d99e1c)"></div>
  <div class="press__cover" role="img" aria-label="Photo magazine cover in sepia" style="left:206px;top:202px;background:linear-gradient(#f0ece6 0 16%,#b8ada2 16%,#6d625a 60%,#3a332e)"></div>
</aside>

<footer class="footer">
  <div class="footer__col" style="left:102px"><h5>Quick Links</h5><ul><li>Home</li><li>Destinations</li><li>Tours</li><li>Holiday types</li><li>About us</li><li>Blog</li></ul></div>
  <div class="footer__col" style="left:295px"><h5>Our Lanternpath</h5><ul><li>Thailand</li><li>Indonesia</li><li>laos</li><li>Cambodia</li><li>Japan</li><li>Myanmar</li></ul></div>
  <div class="footer__col" style="left:484px"><h5>About Lanternpath Journeys</h5><ul><li>Why book with us</li><li>About us</li><li>Meet the team</li><li>Careers</li><li>In the press</li><li>Affiliate Program</li></ul></div>
  <div class="footer__col" style="left:761px"><h5>Newsletter</h5><p>Subscribe to our newsletter and we'll keep you up-to-date. We don't do spam.</p><div class="newsletter">Enter your email address...<b>OK</b></div></div>
  <div class="footer__rule"></div><div class="footer__rule footer__rule--end"></div>
  <div class="footer__social" aria-label="Social links"><i></i><i></i><i></i><i></i><i></i></div>
  <div class="footer__copy">© 2013 Lanternpath Journeys. All Rights Reserved.</div>
</footer>

</body>
</html>
```